Business Card Design

I need a business card for a company based in London, UK. I provide garden design, landscaping and maintenance services. The company specialises in modern, urban gardens. It must be horizontal design, white paper and black simple (easy to read) font. The print must be on clear, white surrounding. I like design that use the colours black, yellow, grey and different shades of green. The design must be tidy. It must not be overloaded with decorating. Embodied a small picture of a fragment of garden or plant or leaf in the sun (it must be yellowish and greenish). It would be good if it's "live and energetic". I attached all text and logo that have to appear on the card.

Target Market(s)

architect, property designers, property management companies, large property owners

Industry/Entity Type

Landscaping

Contact Information for Business Card

All the text must be the same as on my old card which I attached.

Requirements
Must have
• modern, simple, tidy, professional look
green, yellow, black colours,
white surrounding,
simple readable black font on clear white surrounding,
a small picture of garden or plant or "sun lights through the tree canopy"
Nice to have
• graduate movement from light green to dark green
Should not have
• old style font,
text must no be placed on pictures or decorations,
red and blue colours,
picture on the reverse

```html
<!DOCTYPE html>
<html lang="en">
<head>
<meta charset="utf-8">
<title>Greenway Terraces – business card</title>
<link rel="stylesheet" href="https://fonts.googleapis.com/css2?family=Lato:wght@300;400;700;900&display=swap">
<style>
  :root {
    --bg: #e9ebe8;
    --paper: #ffffff;
    --green: #1f9a4c;
    --lime: #8cc63f;
    --yellow: #f2e600;
    --ink: #2b2b2b;
  }
  * { box-sizing: border-box; margin: 0; padding: 0; }
  html, body {
    width: 1200px; height: 926px; overflow: hidden;
    background: var(--bg);
    font-family: "Lato", sans-serif;
  }
  .canvas {
    width: 1200px; height: 926px;
    display: flex; align-items: center; justify-content: center; gap: 40px;
  }
  .card {
    position: relative;
    width: 560px; height: 362px;
    background: var(--paper);
    box-shadow: 0 6px 20px rgba(0,0,0,.15);
    overflow: hidden;
  }

  /* Front */
  .brand-name {
    position: absolute; left: 34px; top: 32px;
    font-weight: 700; font-size: 26px; color: var(--ink); letter-spacing: .3px;
  }
  .services-line {
    position: absolute; left: 34px; top: 92px;
    font-weight: 700; font-size: 17px; letter-spacing: 1.6px;
    color: var(--green); text-transform: uppercase;
  }
  .contacts {
    position: absolute; left: 34px; top: 140px;
    list-style: none; font-size: 15px; line-height: 22px; color: var(--ink);
  }
  .contacts b { display: inline-block; width: 22px; font-weight: 900; }
  .scene {
    position: absolute; right: 20px; top: 120px; width: 250px; height: 176px;
    border-radius: 48% 52% 10% 10% / 55% 55% 10% 10%;
    background:
      radial-gradient(circle at 30% 80%, rgba(242,230,0,.55), transparent 45%),
      radial-gradient(ellipse at 65% 35%, #b6d85a 0%, #d7ea9a 55%, rgba(255,255,255,0) 75%);
  }
  .address-band {
    position: absolute; left: 0; right: 0; bottom: 0; height: 50px;
    background: var(--green);
    color: #fff; font-weight: 700; font-size: 15px; letter-spacing: 2.2px;
    display: flex; align-items: center; padding-left: 34px;
  }

  /* Back */
  .card--back { border: 12px solid var(--lime); }
  .service-list { padding: 22px 26px; }
  .service h3 {
    font-weight: 900; font-size: 16px; color: var(--green);
    text-transform: uppercase; letter-spacing: 1px; line-height: 18px;
  }
  .service p {
    font-weight: 700; font-size: 11.5px; color: var(--ink);
    text-transform: uppercase; letter-spacing: .6px; line-height: 14px;
    margin-bottom: 8px;
  }
</style>
</head>
<body>
<main class="canvas">
  <section class="card card--front">
    <p class="brand-name">Greenway Terraces</p>
    <p class="services-line">Design | Landscaping | Maintenance</p>
    <ul class="contacts">
      <li><b>P</b>02081234567</li>
      <li><b>M</b>07700900123</li>
      <li><b>W</b>www.greenway-terraces.co.uk</li>
      <li><b>E</b>info@greenway-terraces.co.uk</li>
    </ul>
    <div class="scene" role="img" aria-label="Watercolour illustration of slender trees with green canopies and sunlight rising behind soft clouds"></div>
    <div class="address-band">Tomas Wrenfield, 42 Mill Lane, Ashford Vale, KT99 1ZZ</div>
  </section>

  <section class="card card--back">
    <div class="service-list">
      <div class="service">
        <h3>Garden Design</h3>
        <p>All styles, hand drawn &amp; CAD, detailed mapping,<br>underground services tracing, soil analysis</p>
      </div>
      <div class="service">
        <h3>Garden Maintenance</h3>
        <p>Lawn care programes, improving the soil,<br>plant health issues, clearance, tree husbandry</p>
      </div>
      <div class="service">
        <h3>Ground Maintenance</h3>
        <p>Algae, moss &amp; pest control, drainage improvements,<br>green areas, car parks, playgrounds.</p>
      </div>
      <div class="service">
        <h3>Patios, Fences, Decking</h3>
        <p>Railings, walls, driveways,<br>summerhouses, hard &amp; soft wood, natural stone, slabs</p>
      </div>
      <div class="service">
        <h3>Ponds, Irrigation, Lighting</h3>
        <p>Rockeries, water features; Brookvane,<br>Dewline systems; installation &amp; maintenance</p>
      </div>
    </div>
  </section>
</main>
</body>
</html>
```